Need a Web Site Design - Fresh, Modern, and Visually Engaging Website Design

I’m looking to create a clean, modern, and visually appealing website that effectively represents our brand and services. The design should focus on user experience, intuitive navigation, and a professional aesthetic.

The Home page should set the tone for the entire site, featuring a sleek, modern layout with strong visual appeal.

Our Company Logo colors attached. The design can incorporate this color theme or use a unique palette that complements it.

Site Map:
We will begin with the following sections, with the potential to expand and add more services in the future:

Home: A welcoming and engaging introduction to our business, highlighting key services and industries we serve.
About Us: Share our story, mission, and values to connect with visitors.
Software Development: Showcase our expertise in developing innovative software solutions.
Industries We Serve: Provide detailed insights into the sectors we specialize in, including:
- Payroll Sector
- Education
- Transportation
- Home Care Services
Contact Us: Offer easy ways for clients to reach out, including forms and contact details.
Footer: Include essential links, social media handles, and company details.

Draft content for Services Page
Services
We specialize in delivering tailored solutions to meet your business needs. Our expertise spans Product Development, App Development, and Website Development.

1. Product Development
From concept to completion, we help you bring innovative products to life.
What We Offer:
• Custom Software Solutions: Scalable and secure software tailored to your business processes.
• Prototyping & MVP Development: Rapid prototyping and Minimum Viable Product creation to validate ideas.
• End-to-End Development: Comprehensive support from ideation to launch.
• Integration Services: Seamless integration of new products with your existing systems.

2. App Development
Build cutting-edge mobile and desktop applications to engage your audience and enhance operational efficiency.
What We Offer:
• Native & Cross-Platform Apps: Applications built for iOS, Android, and cross-platform frameworks.
• User-Centered Design: Apps designed with intuitive interfaces and smooth user experiences.
• Custom Features: Tailored functionality to meet your unique business needs.
• Maintenance & Updates: Continuous support to keep your app relevant and high-performing.

3. Website Development
Your website is the face of your business. We ensure it leaves a lasting impression.
What We Offer:
• Custom Website Design: Unique and responsive designs tailored to your brand identity.
• E-Commerce Development: Scalable and secure online stores to grow your business.
• CMS Integration: Easy-to-manage content systems like WordPress, Joomla, or custom CMS.
• SEO Optimization: Built-in search engine optimization for enhanced visibility.

Your Journey with Us
Our streamlined approach ensures that your project is handled with precision, creativity, and care. We partner with you at every step to create tailored solutions that transform your business.

Phase One: Discovery
We start by understanding your business inside and out, ensuring the foundation for our partnership is built on knowledge and alignment.
Assessment & Analysis
We dive deep into your business environment to uncover challenges, identify growth opportunities, and understand the economic factors driving your operations.
Process Evaluation
Our team analyzes your current workflows and processes, identifying inefficiencies and areas where improvements can enhance productivity and effectiveness.
Data-Driven Strategy
Using your organization’s technical and operational data, we create informed strategies that align with your goals and drive meaningful outcomes.

Phase Two: Estimate
We present a fully customized solution tailored to your needs, empowering you with the information required to make confident decisions.
Technology Plan & Roadmap
We design a detailed technology roadmap that includes the functionalities you need, the ideal tools and technologies, and a timeline for project completion.
Transition Planning
Our scope includes planning for a seamless transition, covering everything from system migration to user training and long-term usability.
Future Forecasting
Our solutions are built to grow with your business. We consider scalability, future technology trends, and your organization’s long-term needs to ensure lasting success.

Phase Three: Blueprint
Every successful project begins with a comprehensive plan. Our blueprints define every aspect of functionality, technology, and user experience, ensuring a smooth path forward.
Technology and Architecture
We develop a detailed framework outlining the infrastructure, external integrations, security measures, and scalability plans for the project.
Interactive Prototype
We create a clickable prototype that showcases the design, user interface, and functionality of the system, ensuring alignment with your vision.
Engineering & Testing Plan
Our strategy includes step-by-step engineering and rigorous testing for quality, security, and scalability throughout the development process.
Risk Management
We anticipate potential risks and outline mitigation strategies, reducing surprises and keeping the project on track.

Phase Four: Engineering
Our team of expert software engineers transforms the blueprint into a robust, scalable system tailored to your needs.
Full-Service Teams
We assemble a specialized team for your project, ensuring the skills and expertise align with your business goals and technical requirements.
Strategic Delivery
Our phased development approach delivers essential features first, reducing risks and enabling faster time-to-market.
Close Collaboration with Clients
We keep you informed and involved through every sprint, ensuring your vision is realized from the MVP to the final release.

Phase Five: Training & Support
We ensure a smooth integration of your new software, provide training for your team, and offer ongoing support to guarantee success.
Smooth Transition
We work with you to test new modules, retire outdated systems, and ensure a seamless rollout of the new solution.
Teamwide Training
Our team provides comprehensive training, gathers performance feedback, and optimizes the system for peak efficiency.
Long-Term Support
We continue to refine and improve the system post-launch, introducing enhancements to keep you ahead of the curve.

Our Projects
Explore our portfolio of completed projects, each showcasing our commitment to excellence and innovation.
(Provide a visually appealing UI design to display the project list, such as tiles or cards featuring images, project names, and a brief description.)

```html
<!DOCTYPE html>
<html lang="en">
<head>
<meta charset="utf-8">
<title>Nuvara – Tailored Software Solutions</title>
<link href="https://fonts.googleapis.com/css2?family=Poppins:wght@300;400;500;600;700;800&display=swap" rel="stylesheet">
<style>
  :root {
    --pink: #ec008c;
    --blue: #08aeea;
    --ink: #111111;
    --body: #555555;
    --muted: #7a7a7a;
    --white: #ffffff;
    --shadow: 0 10px 30px rgba(0,0,0,0.10);
  }
  * { margin: 0; padding: 0; box-sizing: border-box; }
  html, body { width: 1200px; height: 2362px; overflow: hidden; }
  body { position: relative; background: var(--white); font-family: "Poppins", sans-serif; color: var(--ink); }

  .hero-shape { position: absolute; left: 0; top: 0; width: 1200px; height: 760px; }

  .site-header { position: absolute; left: 0; top: 0; width: 1200px; height: 77px; }
  .brand { position: absolute; left: 132px; top: 20px; font-size: 27px; font-weight: 500; color: var(--white); letter-spacing: 0.2px; }
  .main-nav { position: absolute; left: 489px; top: 30px; display: flex; gap: 21px; }
  .main-nav a { font-size: 13.5px; color: var(--white); text-decoration: none; }
  .contact-btn { position: absolute; left: 921px; top: 25px; width: 114px; height: 29px; border-radius: 15px; background: var(--white); color: var(--ink); font-size: 13px; display: flex; align-items: center; justify-content: center; text-decoration: none; }
  .search-icon { position: absolute; left: 1047px; top: 29px; }

  .hero-copy { position: absolute; left: 188px; top: 325px; width: 400px; color: var(--white); }
  .hero-kicker { font-size: 21px; font-weight: 400; line-height: 1.3; }
  .hero-title { font-size: 42px; font-weight: 700; line-height: 44px; margin-top: 4px; letter-spacing: -0.3px; }
  .hero-lead { font-size: 16px; line-height: 24px; margin-top: 6px; width: 330px; }

  .scroll-cue { position: absolute; left: 1024px; top: 607px; display: flex; align-items: center; gap: 12px; color: var(--white); font-size: 13px; }
  .scroll-cue .ring { width: 30px; height: 30px; border: 1.5px solid var(--white); border-radius: 50%; display: flex; align-items: center; justify-content: center; }

  .about-photo { position: absolute; left: 153px; top: 851px; width: 486px; height: 380px; border-radius: 16px; background: linear-gradient(135deg, #d9dde2 0%, #b9c3cf 45%, #8c96a3 100%); }
  .feature-card { position: absolute; top: 1116px; width: 209px; height: 200px; background: var(--white); border-radius: 14px; box-shadow: var(--shadow); padding: 26px 30px; }
  .feature-card.web { left: 226px; }
  .feature-card.market { left: 453px; }
  .feature-card svg { display: block; height: 52px; }
  .feature-card h3 { font-size: 16.5px; font-weight: 600; margin-top: 12px; }
  .feature-card p { font-size: 13px; line-height: 20px; color: var(--muted); margin-top: 6px; font-weight: 300; }

  .about-copy { position: absolute; left: 709px; top: 882px; width: 350px; }
  .about-copy h2 { font-size: 40px; font-weight: 600; line-height: 1.1; }
  .about-copy p { font-size: 13.3px; line-height: 20.8px; color: var(--body); margin-top: 34px; font-weight: 300; }
  .read-more { display: inline-flex; align-items: center; justify-content: center; margin-top: 30px; width: 130px; height: 33px; border-radius: 17px; background: var(--pink); color: var(--white); font-size: 13px; font-weight: 600; text-decoration: none; }

  .dev-shape { position: absolute; left: 0; top: 1380px; width: 1200px; height: 760px; }
  .dev-intro { position: absolute; left: 200px; top: 1532px; width: 780px; color: var(--white); }
  .dev-intro h2 { font-size: 39px; font-weight: 600; line-height: 1.2; }
  .dev-intro p { font-size: 13.3px; line-height: 20.8px; margin-top: 20px; font-weight: 300; }

  .phase-card { position: absolute; top: 1704px; width: 252px; height: 250px; background: var(--white); border-radius: 14px; box-shadow: var(--shadow); padding: 46px 42px 0; }
  .phase-card.design { left: 193px; }
  .phase-card.blueprint { left: 473px; padding-left: 37px; }
  .phase-card.deploy { left: 755px; }
  .phase-card svg { display: block; height: 54px; }
  .phase-card h3 { font-size: 20px; font-weight: 600; margin-top: 24px; }
  .phase-card p { font-size: 13px; line-height: 20px; color: var(--muted); margin-top: 10px; font-weight: 300; width: 170px; }

  .progress-title { position: absolute; left: 0; top: 2232px; width: 1200px; text-align: center; font-size: 54px; font-weight: 600; color: #7a7a7a; }
</style>
</head>
<body>

  <svg class="hero-shape" viewBox="0 0 1200 760" aria-hidden="false">
    <defs>
      <linearGradient id="officeTones" x1="0" y1="0" x2="1" y2="1">
        <stop offset="0" stop-color="#7fb9c4"/>
        <stop offset="0.35" stop-color="#c9d6d8"/>
        <stop offset="0.65" stop-color="#5f7c92"/>
        <stop offset="1" stop-color="#2f4a66"/>
      </linearGradient>
    </defs>
    <path fill="var(--pink)" d="M0,0 H1200 V634 C980,700 620,760 300,746 C180,740 80,705 0,668 Z"/>
    <path fill="url(#officeTones)" role="img" aria-label="Photo of a team meeting around a table in a bright glass office"
          d="M0,77 H1106 C1165,190 1170,390 1070,545 C975,680 800,718 560,724 C350,730 150,700 0,668 Z"/>
    <ellipse cx="363" cy="442" rx="256" ry="227" fill="var(--blue)"/>
  </svg>

  <header class="site-header">
    <div class="brand">Nuvara</div>
    <nav class="main-nav">
      <a href="#">Home</a>
      <a href="#">About Us</a>
      <a href="#">Services</a>
      <a href="#">Discovery</a>
      <a href="#">Training &amp; Support</a>
    </nav>
    <a class="contact-btn" href="#">Contact Us</a>
    <svg class="search-icon" width="22" height="22" viewBox="0 0 22 22" fill="none" stroke="#fff" stroke-width="1.6">
      <circle cx="9.5" cy="9.5" r="7.5"/><line x1="15" y1="15" x2="20" y2="20"/>
    </svg>
  </header>

  <section class="hero-copy">
    <p class="hero-kicker">We specialize in delivering</p>
    <h1 class="hero-title">Tailored solutions to meet your business needs</h1>
    <p class="hero-lead">Our expertise spans Product Development, App Development, and Website Development.</p>
  </section>

  <div class="scroll-cue">
    <span>Scroll</span>
    <span class="ring">
      <svg width="10" height="12" viewBox="0 0 10 12" fill="none" stroke="#fff" stroke-width="1.3"><line x1="5" y1="1" x2="5" y2="11"/><polyline points="1.5,7.5 5,11 8.5,7.5"/></svg>
    </span>
  </div>

  <div class="about-photo" role="img" aria-label="Photo of four colleagues smiling around a laptop in an office"></div>

  <article class="feature-card web">
    <svg viewBox="0 0 52 52" width="52">
      <circle cx="26" cy="22" r="14" fill="#ffc83d"/>
      <rect x="20" y="36" width="12" height="8" rx="2" fill="#4a5563"/>
      <line x1="26" y1="16" x2="26" y2="34" stroke="#e8710a" stroke-width="2"/>
    </svg>
    <h3>Web solution</h3>
    <p>Lörem ipsum norägisk pseudoning. Valedes mikroning.</p>
  </article>

  <article class="feature-card market">
    <svg viewBox="0 0 52 52" width="52">
      <path d="M24,6 A20,20 0 1 0 44,28 L24,28 Z" fill="#5cb7f0"/>
      <path d="M28,2 A20,20 0 0 1 48,22 L28,22 Z" fill="#ffc83d"/>
      <path d="M48,26 A20,20 0 0 1 40,40 L28,26 Z" fill="#f0506e"/>
    </svg>
    <h3>Market Analysis</h3>
    <p>Lörem ipsum norägisk pseudoning. Valedes mikroning.</p>
  </article>

  <section class="about-copy">
    <h2>About us</h2>
    <p>Lörem ipsum norägisk pseudoning. Valedes mikroning. Nyrägon gäri. Dialig ben tempogram i homoling porede. Mire kontraska.<br>Mirar astrosion tills nykanyll epigt och rälura. Prekir poda bende att homon, plareliga. Far denat nyl inte teonetik. Rebesam tonårsskrämma i prolog. Äbär fädiliga vanyde. Ad min, utom exoling. Disk mikrol. Lanas noligt överklassafari. Por nanade. Eurosm plara. Snippgympa podda krovis. Oska.</p>
    <a class="read-more" href="#">Read More</a>
  </section>

  <svg class="dev-shape" viewBox="0 1380 1200 760" aria-hidden="true">
    <path fill="var(--pink)" d="M0,1486 C250,1425 480,1398 680,1402 C900,1408 1070,1505 1070,1642 C1070,1800 900,1928 700,1992 C460,2062 220,2098 0,2118 Z"/>
  </svg>

  <section class="dev-intro">
    <h2>Software Development</h2>
    <p>Lörem ipsum norägisk pseudoning. Valedes mikroning. Nyrägon gäri. Dialig ben tempogram i homoling porede. Mire kontraska. Mirar astrosion tills nykanyll epigt och rälura. Prekir poda bende att homon, plareliga. Far denat nyl inte teonetik. Rebesam tonårsskrämma i prolog.</p>
  </section>

  <article class="phase-card design">
    <svg viewBox="0 0 54 54" width="54">
      <rect x="4" y="4" width="44" height="34" rx="3" fill="#4b4fa6"/>
      <rect x="10" y="10" width="20" height="20" fill="#f0506e"/>
      <polygon points="26,28 40,28 33,16" fill="#5cb7f0"/>
      <line x1="4" y1="48" x2="52" y2="48" stroke="#9fc3e8" stroke-width="3"/>
    </svg>
    <h3>Design Phase</h3>
    <p>Lörem ipsum norägisk pseudoning. Valedes mikroning.</p>
  </article>

  <article class="phase-card blueprint">
    <svg viewBox="0 0 54 54" width="54">
      <rect x="3" y="8" width="48" height="38" rx="3" fill="#1f8fd6"/>
      <rect x="9" y="14" width="36" height="26" fill="none" stroke="#a9dcff" stroke-width="2"/>
      <line x1="21" y1="14" x2="21" y2="40" stroke="#a9dcff" stroke-width="2"/>
      <line x1="33" y1="14" x2="33" y2="40" stroke="#a9dcff" stroke-width="2"/>
    </svg>
    <h3>Blueprint</h3>
    <p>Lörem ipsum norägisk pseudoning. Valedes mikroning.</p>
  </article>

  <article class="phase-card deploy">
    <svg viewBox="0 0 54 54" width="54">
      <path d="M46,6 L30,10 L14,30 L24,40 L44,24 Z" fill="#e9edf2"/>
      <circle cx="32" cy="22" r="5" fill="#1f8fd6"/>
      <path d="M14,30 L6,32 L12,24 Z M24,40 L22,48 L30,42 Z" fill="#f0506e"/>
      <path d="M16,38 L8,48 L12,40 Z" fill="#ffc83d"/>
    </svg>
    <h3>Deployment</h3>
    <p>Lörem ipsum norägisk pseudoning. Valedes mikroning.</p>
  </article>

  <h2 class="progress-title">In Progress</h2>

</body>
</html>
```